I need a label design to go on our jars of honey. Our company is called Quillbrook Honey Co. The type of honey is called Marram Glade Honey. The jars are 1kg. Attached is the label size. Left hand side needs to have nutritional info... as attached. Middle section is our company name, honey type, 1kg & Kereru Cove, NZ. Right hand side needs to have info as per photo (raw honey etc). I would like to upload more pictures... but I’m unsure how to do this? Thanks, Noreen

Target Market(s)

Honey consumers... families

Industry/Entity Type

Food Production

Colors

Designer to choose colors to be used in the design.

Requirements
Must have
• Nutritional info as per upload
• Type of honey & company name as per upload
• 1kg
• Address
Nice to have
• Similar fonts to upload.
• Possibly background image... floral or beach... very faint though.

```html
<!DOCTYPE html>
<html lang="en">
<head>
<meta charset="utf-8">
<title>Quillbrook Honey Co. – Marram Glade Honey Label</title>
<link rel="stylesheet" href="https://fonts.googleapis.com/css2?family=Oswald:wght@300&family=Arimo:wght@400;700&display=swap">
<style>
  :root {
    --page-bg: #f4f4f2;
    --label-yellow: #e3bd17;
    --label-yellow-light: #efcc2a;
    --label-yellow-deep: #d2a90f;
    --ink-white: #ffffff;
    --ink-soft: rgba(255,255,255,0.88);
    --table-ink: #1d1d1d;
    --table-rule: #222222;
  }
  * { box-sizing: border-box; margin: 0; padding: 0; }
  html, body { width: 1200px; height: 1200px; overflow: hidden; }
  body {
    background: var(--page-bg);
    display: flex; align-items: center; justify-content: center;
  }
  .label {
    width: 1140px; height: 560px;
    display: grid; grid-template-columns: 380px 380px 380px;
    background: linear-gradient(90deg, var(--label-yellow-deep) 0%, var(--label-yellow) 20%, var(--label-yellow-light) 50%, var(--label-yellow) 80%, var(--label-yellow-light) 100%);
  }
  .panel { position: relative; padding: 36px 30px; }

  /* Left: nutrition */
  .panel--nutrition { display: flex; flex-direction: column; align-items: center; }
  .claim {
    font-family: "Arimo", sans-serif; font-size: 14px; line-height: 1.15;
    color: var(--ink-soft); text-align: center; margin-bottom: 6px;
  }
  .nutrition {
    width: 100%; background: var(--ink-white); border: 2px solid var(--table-rule);
    font-family: "Arimo", sans-serif; color: var(--table-ink);
  }
  .nutrition__title { font-weight: 700; font-size: 17px; padding: 3px 6px 0; letter-spacing: 0.3px; border-bottom: 1px solid var(--table-rule); }
  .nutrition__meta { font-size: 13.5px; padding: 2px 6px; line-height: 1.45; border-bottom: 2px solid var(--table-rule); }
  .nutrition table { width: 100%; border-collapse: collapse; font-size: 16px; }
  .nutrition th { font-weight: 400; font-size: 13px; line-height: 1.1; text-align: left; color: #444; padding: 4px 0 6px; border-bottom: 2px solid var(--table-rule); vertical-align: top; }
  .nutrition td { padding: 1px 0; line-height: 1.3; }
  .nutrition td:first-child, .nutrition th:first-child { padding-left: 6px; width: 42%; }
  .nutrition tbody tr:first-child td { padding-top: 8px; }
  .storage {
    font-family: "Arimo", sans-serif; font-size: 13.5px; line-height: 1.3;
    color: var(--ink-soft); text-align: center; margin: 8px 0 10px;
  }
  .batch {
    width: 78%; background: var(--ink-white); padding: 6px 8px;
    font-family: "Arimo", sans-serif; font-weight: 700; font-size: 15px; color: var(--table-ink);
    display: grid; grid-template-columns: 90px 1fr; row-gap: 2px;
  }

  /* Middle: brand */
  .panel--brand {
    display: flex; flex-direction: column; align-items: center; text-align: center;
    color: var(--ink-white); padding-top: 56px;
    font-family: "Oswald", sans-serif; font-weight: 300;
  }
  .brand__company { font-weight: 300; font-size: 34px; line-height: 1.25; letter-spacing: 1px; }
  .brand__product { font-weight: 300; font-size: 56px; line-height: 1.1; margin-top: 34px; }
  .brand__weight, .brand__origin { font-size: 26px; letter-spacing: 1px; }
  .brand__weight { margin-top: 34px; }
  .brand__origin { margin-top: 22px; }

  /* Right: info */
  .panel--info {
    display: flex; flex-direction: column; align-items: center; justify-content: center; gap: 22px;
    text-align: center; font-family: "Oswald", sans-serif; font-weight: 300;
    font-size: 15px; letter-spacing: 0.5px; line-height: 1.6; color: var(--ink-soft); text-transform: uppercase;
  }
</style>
</head>
<body>
  <main class="label">
    <section class="panel panel--nutrition">
      <p class="claim">100% New Zealand Honey<br>No added ingredients</p>
      <div class="nutrition">
        <div class="nutrition__title">NUTRITIONAL INFORMATION</div>
        <div class="nutrition__meta">Serving per package: 100<br>Serving size: 10g</div>
        <table>
          <thead>
            <tr><th></th><th>Average<br>Quantity<br>per Serving</th><th>Average<br>Quantity<br>per 100g</th></tr>
          </thead>
          <tbody>
            <tr><td>Energy</td><td>134kj</td><td>1340kj</td></tr>
            <tr><td>Protein</td><td>0.04g</td><td>0.4g</td></tr>
            <tr><td>Fat total</td><td>0g</td><td>0g</td></tr>
            <tr><td>- saturated</td><td>0g</td><td>0g</td></tr>
            <tr><td>Carbohydrate</td><td>7.9g</td><td>79.6g</td></tr>
            <tr><td>- sugars</td><td>7.8g</td><td>78.1g</td></tr>
            <tr><td>Sodium</td><td>1.2mg</td><td>12mg</td></tr>
          </tbody>
        </table>
      </div>
      <p class="storage">Store upright in a cool, dry place.<br>No refridgeration needed.<br>Not recommended for infants below<br>the age of 12 months.</p>
      <div class="batch">
        <span>Best before</span><span>:</span>
        <span>RMP</span><span>:</span>
        <span>Batch No</span><span>:</span>
      </div>
    </section>

    <section class="panel panel--brand">
      <h1 class="brand__company">Quillbrook<br>Honey Co.</h1>
      <h2 class="brand__product">Marram Glade<br>Honey</h2>
      <p class="brand__weight">1KG</p>
      <p class="brand__origin">Kereru Cove N.Z.</p>
    </section>

    <section class="panel panel--info">
      <p>Raw honey from our own hives<br>Unheated and unfiltered</p>
      <p>Natural honey may crystallise &amp;<br>this is normal as it contains<br>all its natural goodness!</p>
      <p>Handmade<br>with care in NZ</p>
      <p>This honey is prized for its<br>lovely flavour</p>
      <p>www.quillbrookhoney.co.nz<br>14 Kauri Lane<br>Kereru Cove<br>New Zealand</p>
    </section>
  </main>
</body>
</html>
```